Veltiwell- Comprehensive quality healthcare delivered at your door.

I am looking for brochures to help promote my business. My business name is Veltiwel (see attachment and logo). This is a new health delivery system designed to provide high quality care to elderly in their communities or at home.

See attachements. The logo is already designed.

As far as services provided (see attachment)

Target Market(s)

Elderly patients

Industry/Entity Type

Business

Font styles to use
Serif

Colors

Designer to choose colors to be used in the design.

```html
<!DOCTYPE html>
<html lang="en">
<head>
<meta charset="utf-8">
<title>Veltiwel Brochure</title>
<link href="https://fonts.googleapis.com/css2?family=Jost:wght@400;500;700&display=swap" rel="stylesheet">
<style>
  :root {
    --bg: #eeeae4;
    --forest: #243300;
    --orange: #f39a1c;
    --orange-soft: #f6b44f;
    --leaf: #6b8a2e;
    --white: #ffffff;
    --ink: #1f2a10;
  }
  * { margin: 0; padding: 0; box-sizing: border-box; }
  html, body {
    width: 1200px; height: 1200px; overflow: hidden;
    background: var(--bg);
    font-family: "Jost", "Futura", sans-serif;
  }
  .brochure {
    position: absolute; left: 93px; top: 208px;
    width: 1014px; height: 784px;
    background: var(--white);
    box-shadow: 0 4px 14px rgba(0,0,0,0.18);
    display: flex;
  }
  .panel { position: relative; width: 338px; height: 100%; }
  .photo { position: absolute; left: 0; top: 0; width: 100%; height: 442px; }
  .photo-care { background: linear-gradient(160deg, #e9e3da 0%, #b8c7d8 40%, #2f6fb5 75%, #d9d2c6 100%); }
  .photo-hand { background: linear-gradient(180deg, #ffffff 0%, #f1ddd2 45%, #e2b9a6 70%, #f6f0ea 100%); }
  .photo-visit { background: linear-gradient(160deg, #f3f4f5 0%, #bfe3e0 40%, #c9ccd3 70%, #8c8f96 100%); }
  .band { position: absolute; left: 0; top: 442px; width: 100%; height: 36px; background: var(--orange-soft); }
  .band-header { display: flex; background: var(--orange); }
  .band-header h2 {
    flex: 1; color: var(--white); font-weight: 400; font-size: 20px;
    line-height: 36px; padding-left: 37px; letter-spacing: 0.2px;
  }
  .band-header .accent { width: 37px; background: var(--leaf); }
  .services {
    position: absolute; left: 0; top: 478px; width: 100%; bottom: 0;
    background: var(--forest); color: var(--white);
    padding: 16px 30px 0 37px;
  }
  .services ul { list-style: none; font-size: 13.6px; line-height: 16.9px; }
  .services li { position: relative; padding-left: 15px; }
  .services li::before { content: "•"; position: absolute; left: 0; }
  .contact-block {
    position: absolute; top: 478px; left: 0; width: 100%; height: 268px;
    display: flex; flex-direction: column; justify-content: center; align-items: center;
    text-align: center; color: var(--ink); font-size: 15px; line-height: 19px;
    background: linear-gradient(90deg, #fff 0%, #fff 75%, #ebebeb 100%);
  }
  .contact-block p + p { margin-top: 18px; }
  .contact-block b { font-weight: 700; }
  .strip {
    position: absolute; left: 0; bottom: 0; width: 100%; height: 38px;
    background: var(--forest); color: var(--white);
    font-size: 15.5px; line-height: 38px; text-align: center; letter-spacing: 0.3px;
  }
  .brand {
    position: absolute; top: 478px; left: 0; width: 100%; height: 268px;
    display: flex; flex-direction: column; align-items: center; justify-content: center;
  }
  .brand-dot { width: 110px; height: 110px; border-radius: 50%; background: var(--orange); margin-bottom: 16px; }
  .brand-name { color: var(--forest); font-weight: 400; font-size: 36px; letter-spacing: 0.5px; }
</style>
</head>
<body>
  <div class="brochure">
    <section class="panel panel-services">
      <div class="photo photo-care" role="img" aria-label="Photo of a smiling nurse in blue scrubs with an elderly woman in a wheelchair"></div>
      <div class="band band-header"><h2>OUR SERVICES</h2><span class="accent"></span></div>
      <div class="services">
        <ul>
          <li>Comprehensive primary care services</li>
          <li>Coordination of speciality care</li>
          <li>Chronic disease management such as COPD, Asthma, Diabetes mellitus, Heart disease like congestive heart failure, Alzheimer's dementia, etc…</li>
          <li>Transitional Care</li>
          <li>Skilled nursing visits for wound care, catheter care, ostomy</li>
          <li>Social services assessment</li>
          <li>Home health assistance</li>
          <li>Physical therapy</li>
          <li>Mental health</li>
          <li>Dental health</li>
          <li>Transportation</li>
        </ul>
      </div>
    </section>

    <section class="panel panel-contact">
      <div class="photo photo-hand" role="img" aria-label="Photo of an elderly hand resting on a wooden walking cane"></div>
      <div class="band"></div>
      <div class="contact-block">
        <p>2400 Meadowlark Ln #200,<br>Fairhaven, TX 78010, USA</p>
        <p>Hours <b>Open today · 8AM–7PM</b></p>
        <p>Phone <b>+1 555 0142 88</b><br>Email <b>info@veltiwel.com</b></p>
      </div>
      <div class="strip"></div>
    </section>

    <section class="panel panel-cover">
      <div class="photo photo-visit" role="img" aria-label="Photo of a nurse in teal scrubs talking with an elderly man on a sofa"></div>
      <div class="band"></div>
      <div class="brand">
        <span class="brand-dot"></span>
        <span class="brand-name">VELTIWEL</span>
      </div>
      <div class="strip">+1 555 0142 88 | info@veltiwel.com</div>
    </section>
  </div>
</body>
</html>
```